Business Card design for shipping company 'FERNHOLT INTERNATIONAL LTD'

Classic / traditional business card in black Garamond / Times New Roman or similar text for a shipping / marine transport company, containing the following information:

QUOTE

FERNHOLT INTERNATIONAL LTD

MARTIN QUESTEDGE FICS

T: +44 7902 615370
E: cargo@fernholt-example.com

UNQUOTE

Target Market(s)

Marine / Shipping industry

Contact Information for Business Card

FERNHOLT INTERNATIONAL LTD MARTIN QUESTEDGE FICS T: +44 7902 615370 E: cargo@fernholt-example.com

Font styles to use
Serif

Colors

Designer to choose colors to be used in the design.

Requirements
Must have
• Garamond / Times New Roman or similar text in black colour

```html
<!DOCTYPE html>
<html lang="en">
<head>
<meta charset="utf-8">
<title>Fernholt International Ltd – Business Card</title>
<link rel="stylesheet" href="https://fonts.googleapis.com/css2?family=EB+Garamond:wght@400&family=Tinos:wght@400;700&display=swap">
<style>
  :root {
    --page-bg: #e6e6e6;
    --card-white: #ffffff;
    --field-tint: #f3f8fd;
    --band-light-edge: #7aaddb;
    --band-light-centre: #c9def0;
    --band-deep: #0676bb;
    --band-navy: #1255a8;
    --band-sheen: #7aaddb;
    --notch-fill: #c9def0;
    --ink: #231f20;
  }
  html, body {
    margin: 0;
    padding: 0;
    width: 1200px;
    height: 1200px;
    overflow: hidden;
    background: var(--page-bg);
  }
  .artboard {
    display: block;
    width: 1200px;
    height: 1200px;
  }
  .company-name {
    font-family: "EB Garamond", "Times New Roman", serif;
    font-size: 58px;
    fill: var(--ink);
  }
  .holder-name {
    font-family: "Tinos", "Times New Roman", serif;
    font-weight: 700;
    font-size: 50px;
    fill: var(--ink);
  }
  .contact-line {
    font-family: "Tinos", "Times New Roman", serif;
    font-size: 40px;
    fill: var(--ink);
  }
  .icon-ring {
    fill: none;
    stroke: var(--ink);
    stroke-width: 2.5;
  }
  .icon-glyph { fill: var(--ink); }
</style>
</head>
<body>
<svg class="artboard" viewBox="0 0 1932 1932" xmlns="http://www.w3.org/2000/svg" aria-labelledby="card-title">
  <title id="card-title">Fernholt International Ltd business card for Martin Questedge FICS</title>
  <defs>
    <linearGradient id="title-band-fill" x1="0" y1="0" x2="1" y2="0">
      <stop offset="0" stop-color="var(--band-light-edge)"/>
      <stop offset="0.5" stop-color="var(--band-light-centre)"/>
      <stop offset="1" stop-color="var(--band-light-edge)"/>
    </linearGradient>
    <linearGradient id="contact-band-fill" x1="320" y1="1178" x2="1613" y2="899" gradientUnits="userSpaceOnUse">
      <stop offset="0" stop-color="var(--band-navy)"/>
      <stop offset="0.22" stop-color="var(--band-deep)"/>
      <stop offset="0.5" stop-color="var(--band-sheen)"/>
      <stop offset="0.75" stop-color="var(--band-deep)"/>
      <stop offset="1" stop-color="var(--band-navy)"/>
    </linearGradient>
  </defs>

  <g class="card">
    <rect class="card-base" x="320" y="578" width="1293" height="776" fill="var(--card-white)"/>

    <g class="card-field" role="img" aria-label="Pale blue diagonal chevron line pattern on white">
      <rect x="320" y="582" width="1293" height="131" fill="var(--field-tint)"/>
      <rect x="320" y="801" width="1293" height="98" fill="var(--field-tint)"/>
      <rect x="320" y="1178" width="1293" height="90" fill="var(--field-tint)"/>
    </g>

    <rect class="title-band" x="319" y="713" width="1294" height="88" fill="url(#title-band-fill)"/>
    <rect class="contact-band" x="320" y="899" width="1293" height="279" fill="url(#contact-band-fill)"/>

    <g class="footer-band">
      <rect x="320" y="1268" width="1293" height="86" fill="var(--band-light-edge)"/>
      <polygon points="1088,1268 1310,1268 1222,1354 1190,1354" fill="var(--card-white)"/>
      <polygon points="1108,1268 1292,1268 1206,1351" fill="var(--notch-fill)"/>
    </g>

    <text class="company-name" x="497" y="781" textLength="940" lengthAdjust="spacingAndGlyphs">FERNHOLT INTERNATIONAL LTD</text>

    <text class="holder-name" x="697" y="982" textLength="563" lengthAdjust="spacingAndGlyphs">MARTIN QUESTEDGE FICS</text>

    <g class="contact-phone">
      <circle class="icon-ring" cx="801" cy="1074" r="19"/>
      <path class="icon-glyph" d="M789 1067 q12 -8 24 0 l-2 4 h-5 v-3 q-5 -2 -10 0 v3 h-5 z"/>
      <rect class="icon-glyph" x="790" y="1073" width="22" height="12" rx="2"/>
      <circle cx="801" cy="1079" r="3.5" fill="var(--card-white)"/>
      <text class="contact-line" x="832" y="1088" textLength="270" lengthAdjust="spacingAndGlyphs">+44 7902 615370</text>
    </g>

    <g class="contact-email">
      <circle class="icon-ring" cx="680" cy="1121" r="19"/>
      <rect class="icon-glyph" x="668" y="1112" width="24" height="17" rx="1.5"/>
      <path d="M669 1113 l11 9 l11 -9 M669 1128 l8 -7 M691 1128 l-8 -7" fill="none" stroke="var(--card-white)" stroke-width="1.6"/>
      <text class="contact-line" x="713" y="1135" textLength="445" lengthAdjust="spacingAndGlyphs">cargo@fernholt-example.com</text>
    </g>
  </g>
</svg>
</body>
</html>
```